Label for a new brand of Straight Bourbon

The brand name for this Straight Bourbon is Harrowfield Pass, the origin for the look and feel derives from the history of Silas Pennock marking this trail for settlers going west and became one of the first English speaking settlements, you can find more about it here https://www.pastchronicle-example.com/topics/frontier-routes/timber-trace
that region is very famous for the production of Bourbon.
The proof will be 90, alc. by vol. 45% Vol 750 ML.

```html
<!DOCTYPE html>
<html lang="en">
<head>
<meta charset="utf-8">
<title>Harrowfield Pass Straight Bourbon Label</title>
<link rel="stylesheet" href="https://fonts.googleapis.com/css2?family=Merriweather:wght@700;900&family=UnifrakturMaguntia&family=Raleway:wght@400&display=swap">
<style>
  :root {
    --ink: #2a2a2a;
    --label-bg: #2b2b2b;
    --silver: #a6a6a6;
    --silver-line: #9c9c9c;
  }
  html, body {
    margin: 0;
    padding: 0;
    width: 1200px;
    height: 1200px;
    overflow: hidden;
    background: var(--label-bg);
  }
  .label {
    display: block;
    width: 1200px;
    height: 1200px;
  }
  .brand-name {
    font-family: "Merriweather", Georgia, serif;
    font-weight: 900;
    font-size: 16px;
    fill: var(--ink);
    letter-spacing: 0.3px;
  }
  .style-kicker {
    font-family: "Merriweather", Georgia, serif;
    font-weight: 700;
    font-size: 16px;
    letter-spacing: 3px;
    fill: var(--ink);
  }
  .style-title {
    font-family: "UnifrakturMaguntia", "Old English Text MT", serif;
    font-size: 104px;
    fill: var(--ink);
  }
  .star-row {
    font-family: "Raleway", Arial, sans-serif;
    font-size: 11px;
    fill: var(--silver);
    letter-spacing: 3.6px;
  }
  .volume-note {
    font-family: "Raleway", Arial, sans-serif;
    font-weight: 400;
    font-size: 19px;
    fill: var(--silver);
  }
</style>
</head>
<body>
<svg class="label" viewBox="0 0 567 567" xmlns="http://www.w3.org/2000/svg" aria-label="Harrowfield Pass Straight Bourbon label">
  <!-- inner frame -->
  <rect class="inner-frame" x="175" y="68" width="217" height="432" fill="none" stroke="var(--silver-line)" stroke-width="1.6"/>

  <!-- outer shield -->
  <path class="shield-outline"
        d="M283,30 Q205,108 112,122 Q88,172 98,222 L98,325 Q90,400 112,455 Q205,470 283,538 Q361,470 455,455 Q477,400 469,325 L469,222 Q479,172 455,122 Q361,108 283,30 Z"
        fill="var(--label-bg)" stroke="var(--silver)" stroke-width="5"/>
  <rect class="inner-frame-front" x="175" y="68" width="217" height="432" fill="none" stroke="var(--silver-line)" stroke-width="1.6"/>

  <!-- small floral ornaments -->
  <circle class="ornament-top" cx="283" cy="80" r="9" fill="var(--silver)" role="img" aria-label="Small four-petal flower ornament"/>
  <circle class="ornament-bottom" cx="283" cy="470" r="9" fill="var(--silver)" role="img" aria-label="Small four-petal flower ornament"/>

  <!-- brand plate -->
  <path class="brand-plate"
        d="M200,120 L367,120 Q372,135 390,140 L390,180 Q372,185 367,198 L200,198 Q195,185 177,180 L177,140 Q195,135 200,120 Z"
        fill="var(--silver)"/>
  <line class="plate-rule" x1="236" y1="132" x2="331" y2="132" stroke="var(--ink)" stroke-width="1.5"/>
  <line class="plate-rule" x1="236" y1="187" x2="331" y2="187" stroke="var(--ink)" stroke-width="1.5"/>
  <text class="brand-name" x="283.5" y="156" text-anchor="middle">HARROWFIELD</text>
  <text class="brand-name" x="283.5" y="179" text-anchor="middle">PASS</text>

  <!-- style banner -->
  <path class="style-banner"
        d="M50,222 L516,222 A12,12 0 0 0 528,234 L528,313 A12,12 0 0 0 516,325 L50,325 A12,12 0 0 0 38,313 L38,234 A12,12 0 0 0 50,222 Z"
        fill="var(--silver)"/>
  <text class="style-kicker" x="245" y="258" text-anchor="middle">STRAIGHT</text>
  <text class="style-title" x="300" y="318" text-anchor="middle" textLength="400" lengthAdjust="spacingAndGlyphs">Bourbon</text>

  <!-- stars -->
  <text class="star-row" x="283.5" y="364" text-anchor="middle">★★★★★★★★★★★★★★</text>

  <!-- volume -->
  <text class="volume-note" x="283.5" y="428" text-anchor="middle">45% BY VOL 750 ML</text>
</svg>
</body>
</html>
```